Flyer Design Project

Just needing a sleek, modern brochure design for my Paint Contracting business. It's a one sided leaflet (99mm X 210mm)

Brennick Finish Coatings
"Over 25 years experience"
"We set the standard for quality and service"

Call for a free estimate:
Dorian Vellacott 0438195026
Dorianvellacott0@mailbox-example.com
http://brennickfinishcoatings.sitenest-example.com.au/

All Painting services offered:
Interior, exterior, pressure washing, staing, roof restoration, residential, commercial and body corporate

Target Market(s)

Home owners

Industry/Entity Type

Business

```html
<!DOCTYPE html>
<html lang="en">
<head>
<meta charset="utf-8">
<title>Brennick Finish Coatings – Flyer</title>
<link rel="stylesheet" href="https://fonts.googleapis.com/css2?family=Fraunces:opsz,wght@144,900&family=Mulish:wght@600;700;800&display=swap">
<style>
:root{
  --green:#0b7a3b;
  --green-dark:#075a2b;
  --orange:#d9621a;
  --cream:#fdf8c9;
  --white:#ffffff;
  --ink:#222222;
  --outline:#1d2a1f;
}
*{box-sizing:border-box;margin:0;padding:0}
html,body{width:1200px;height:2559px;overflow:hidden;background:var(--white)}
.flyer{position:relative;width:1200px;height:2559px;overflow:hidden;background:var(--white);font-family:"Mulish",sans-serif;color:var(--ink)}
.abs{position:absolute}
.header{left:0;top:0;width:1200px;height:471px;background:var(--green)}
.display{font-family:"Fraunces",serif;font-weight:900;text-align:center;left:0;width:1200px;line-height:1}
.on-green{color:var(--white);text-shadow:0 0 3px var(--outline),4px 4px 0 var(--outline),-2px -2px 0 var(--outline),2px -2px 0 var(--outline),-2px 2px 0 var(--outline)}
.tagline-owner{top:70px;font-size:70px}
.brand-line-1{top:180px;font-size:112px}
.brand-line-2{top:305px;font-size:112px}
.swatch-band{left:0;top:471px;width:1200px;height:400px;background:linear-gradient(160deg,#9fd3e0 0%,#c9e39a 22%,#f4ee8a 42%,#f7c46b 62%,#ef8a55 80%,#ffffff 100%);opacity:.55}
.swatch-fade{left:0;top:620px;width:1200px;height:300px;background:linear-gradient(to bottom,rgba(255,255,255,0),var(--white) 70%)}
.slogan{color:var(--green);-webkit-text-stroke:2px var(--white);text-shadow:3px 3px 6px rgba(0,0,0,.45)}
.experience{top:520px;font-size:66px}
.standard-1{top:620px;font-size:84px}
.standard-2{top:725px;font-size:84px}
.customers{top:848px;font-size:42px;color:var(--orange);letter-spacing:1px}
.customers b{font-size:58px}
.offer-band{left:0;top:917px;width:1200px;height:866px;background:var(--cream)}
.makeover-question{top:955px;font-size:52px;color:var(--green)}
.services{left:128px;top:1100px;list-style:none;font-size:44px;font-weight:700;color:var(--green);line-height:64px}
.services li{position:relative;padding-left:50px}
.services li::before{content:"";position:absolute;left:0;top:21px;width:22px;height:22px;border-radius:50%;background:var(--dot)}
.pricing{left:98px;top:1650px;font-size:31px;font-weight:700;line-height:44px;color:var(--ink)}
.painter{left:860px;top:1000px;width:300px;height:1500px;background:linear-gradient(to bottom,#f0efe9,#d9dbdc 60%,#bfc3c6);border-radius:120px 120px 20px 20px}
.paint-cans{left:591px;top:1954px;width:335px;height:326px;background:radial-gradient(circle at 40% 45%,#f5f5f5,#c4c7ca 70%);border-radius:40px}
.brand-mark{left:106px;top:1800px;display:flex;align-items:center;gap:18px}
.brand-mark .square{width:56px;height:56px;background:var(--green)}
.brand-mark span{font-size:38px;font-weight:800;color:var(--green)}
.contact-call{left:115px;top:1930px;font-size:34px;font-weight:700}
.advice{left:115px;top:2000px;font-size:31px;font-weight:700;line-height:46px}
.phone{left:108px;top:2120px;display:flex;align-items:center;gap:14px;font-family:"Fraunces",serif;font-weight:900;font-size:60px;color:var(--orange);text-shadow:2px 2px 0 #6b2a06}
.email{left:115px;top:2240px;font-size:31px;font-weight:700}
.website{left:115px;top:2292px;font-size:25px;font-weight:700;color:var(--green-dark)}
.rule{left:117px;top:2350px;width:485px;height:4px;background:var(--green-dark)}
.licence{left:108px;top:2372px;display:flex;align-items:center;gap:6px;font-size:32px;line-height:42px}
.licence .paren{font-size:92px;font-weight:600;line-height:1}
</style>
</head>
<body>
<main class="flyer">
  <header class="abs header"></header>
  <p class="abs display on-green tagline-owner">Owner Operators</p>
  <h1 class="abs display on-green brand-line-1">Brennick</h1>
  <p class="abs display on-green brand-line-2">Finish Coatings</p>

  <div class="abs swatch-band" role="img" aria-label="Fanned paint colour swatch cards in blue, green, yellow and orange"></div>
  <div class="abs swatch-fade"></div>

  <p class="abs display slogan experience">Over 25 years experience</p>
  <p class="abs display slogan standard-1">We set the standard</p>
  <p class="abs display slogan standard-2">for quality and service</p>
  <p class="abs display customers">OVER <b>1500</b> SATISFIED CUSTOMERS</p>

  <section class="abs offer-band"></section>
  <h2 class="abs display makeover-question">Is it time to have a makeover?</h2>

  <ul class="abs services">
    <li style="--dot:#e0222b">Painting Makeovers</li>
    <li style="--dot:#e0641c">Pressure Washing</li>
    <li style="--dot:#b05a9a">Stain Work</li>
    <li style="--dot:#f2e20f">Roof Repainting</li>
    <li style="--dot:#1e9ad6">Professional Decorators</li>
    <li style="--dot:#7a3fa0">Residential, Commercial<br>&amp; Body Corporate</li>
    <li style="--dot:#0b8a3e">Great value &amp; Friendly Service</li>
  </ul>

  <p class="abs pricing">Internal Makeovers From $3,000 ex gst<br>Finance Assistance to approved applicants</p>

  <div class="abs painter" role="img" aria-label="Painter in white overalls and green cap, seen from behind, reaching up with a long-handled paint roller"></div>
  <div class="abs paint-cans" role="img" aria-label="Group of open paint tins in red, yellow, blue and green"></div>

  <div class="abs brand-mark"><div class="square"></div><span>Brennick Finish Coatings</span></div>

  <p class="abs contact-call">Call Dorian Vellacott</p>
  <p class="abs advice">Free Professional Decorating<br>&nbsp;Advice &amp; Quotation</p>

  <p class="abs phone">
    <svg width="50" height="54" viewBox="0 0 24 24" aria-hidden="true"><path fill="#d9621a" d="M6.6 10.8a15.1 15.1 0 0 0 6.6 6.6l2.2-2.2a1 1 0 0 1 1-.25 11.4 11.4 0 0 0 3.6.57 1 1 0 0 1 1 1V20a1 1 0 0 1-1 1A17 17 0 0 1 3 4a1 1 0 0 1 1-1h3.5a1 1 0 0 1 1 1c0 1.25.2 2.45.57 3.57a1 1 0 0 1-.25 1z"/></svg>
    0438195026
  </p>

  <p class="abs email">Dorianvellacott0@mailbox-example.com</p>
  <p class="abs website">http://brennickfinishcoatings.sitenest-example.com.au/</p>
  <div class="abs rule"></div>
  <div class="abs licence"><span class="paren">(</span><span>BSA # 4827513<br>Fully Insured</span><span class="paren">)</span></div>
</main>
</body>
</html>
```